I need 2 infographic designs about drug use in the US

We require 2 infographic designs for an article about the history of drug use in the US. We're talking about 2 separate infographs, that will appear in the same article, so they should look similar.

We will provide the content and data for both infographics - see attached.

Size: The infographic will be posted on this site: [login to view URL], and should fit the width of its ***inner pages*** (and be readable, of course).

Color palate: Nothing specific in mind - they should be eye-catching, yet understated.

The infographics should be highly professional, and VERY eye-catching.

Here are some examples of infographic designs I like:
[login to view URL]
[login to view URL]
[login to view URL]

Priority will be given to designers who show a portfolio that includes infographic designs.

ATTACHED IS THE CONTENT FOR THE TWO INFOGRAPHICS.

```html
<!DOCTYPE html>
<html lang="en">
<head>
<meta charset="utf-8">
<title>The Introduction of Drugs to the US in the 19th Century</title>
<link rel="stylesheet" href="https://fonts.googleapis.com/css2?family=Anton&family=Arimo:wght@700&display=swap">
<style>
  :root {
    --bg-top: #e53c3a;
    --bg-bottom: #c42a28;
    --header: #1f1d1f;
    --header-accent: #6a4f86;
    --ink: #111111;
    --text: #ffffff;
    --decor-dark: rgba(20, 10, 14, 0.28);
  }
  * { box-sizing: border-box; margin: 0; padding: 0; }
  html, body { width: 1200px; height: 3037px; overflow: hidden; }
  body { font-family: "Arimo", Arial, sans-serif; }
  .infographic {
    position: relative;
    width: 1200px;
    height: 3037px;
    background: linear-gradient(180deg, var(--bg-top) 0%, var(--bg-top) 55%, var(--bg-bottom) 100%);
    overflow: hidden;
  }
  .header {
    position: absolute;
    left: 0; top: 0;
    width: 1200px; height: 133px;
    background: var(--header);
    z-index: 4;
  }
  .header-title {
    position: absolute;
    left: 150px; right: 150px; top: 2px;
    font-family: "Anton", Impact, sans-serif;
    font-weight: 400;
    color: var(--text);
    font-size: 48px;
    line-height: 62px;
    text-align: center;
    letter-spacing: 0.5px;
    text-transform: uppercase;
  }
  .header-title sup { font-size: 24px; vertical-align: 22px; line-height: 0; }
  .header-badge { position: absolute; background: var(--header-accent); }
  .header-badge--left { left: 0; top: 0; width: 120px; height: 120px; clip-path: polygon(0 0, 100% 0, 0 100%); }
  .header-badge--right { right: 0; top: 27px; width: 160px; height: 106px; clip-path: polygon(12% 0, 100% 0, 88% 100%, 0 100%); }

  .decor { position: absolute; z-index: 1; }
  .decor--cup { left: 607px; top: 140px; width: 206px; height: 327px; background: linear-gradient(180deg, #f4f4f4, #d8d8d8); border-radius: 18px 18px 30px 30px; }
  .decor--molecule-top { left: 730px; top: 267px; width: 440px; height: 380px; background: var(--decor-dark); border-radius: 40px; opacity: 0.55; }
  .decor--leaf { left: 427px; top: 1013px; width: 333px; height: 374px; background: radial-gradient(circle at 50% 55%, #1a1216 0%, #2a1620 60%, rgba(42,22,32,0) 72%); }
  .decor--no-smoking { left: 80px; top: 1067px; width: 200px; height: 200px; border-radius: 50%; background: #ffffff; border: 14px solid var(--ink); }
  .decor--skull { left: 580px; top: 1920px; width: 167px; height: 160px; background: radial-gradient(circle at 50% 45%, #ffffff 0%, #e6e6e6 45%, rgba(230,230,230,0) 70%); }
  .decor--molecule-bottom { left: 640px; top: 2053px; width: 507px; height: 707px; background: var(--decor-dark); border-radius: 60px; opacity: 0.5; }
  .decor--no-syringe { left: 620px; top: 2587px; width: 247px; height: 247px; border-radius: 50%; background: #ffffff; border: 16px solid var(--ink); }

  .fact-box { position: absolute; color: var(--text); z-index: 2; }
  .fact-box__frame { position: absolute; inset: 0; width: 100%; height: 100%; z-index: -1; overflow: visible; }
  .fact-box__label {
    position: absolute;
    height: 40px;
    background: var(--header);
    color: var(--text);
    font-family: "Anton", Impact, sans-serif;
    font-weight: 400;
    font-size: 31px;
    line-height: 40px;
    text-align: center;
    text-transform: uppercase;
    clip-path: polygon(4% 0, 100% 0, 96% 100%, 0 100%);
  }
  .fact-box__list {
    position: absolute;
    list-style: none;
    font-size: 37px;
    line-height: 44.7px;
    font-weight: 700;
  }
  .fact-box__list li { position: relative; padding-left: 16px; }
  .fact-box__list li::before {
    content: "";
    position: absolute;
    left: 0; top: 18px;
    width: 8px; height: 8px;
    background: var(--text);
  }
  .fact-box__list sup { font-size: 20px; line-height: 0; }

  .fact-box--morphine { left: 96px; top: 187px; width: 557px; height: 920px; }
  .fact-box--morphine .fact-box__label { left: -5px; top: -11px; width: 236px; }
  .fact-box--morphine .fact-box__list { left: 20px; top: 60px; width: 516px; }

  .fact-box--cocaine { left: 729px; top: 583px; width: 424px; height: 1417px; }
  .fact-box--cocaine .fact-box__label { left: 118px; top: -20px; width: 186px; }
  .fact-box--cocaine .fact-box__list { left: 26px; top: 61px; width: 386px; }

  .fact-box--marijuana { left: 87px; top: 1260px; width: 566px; height: 740px; }
  .fact-box--marijuana .fact-box__label { left: 166px; top: -27px; width: 247px; }
  .fact-box--marijuana .fact-box__list { left: 33px; top: 36px; width: 492px; }

  .fact-box--heroin { left: 91px; top: 2067px; width: 556px; height: 906px; }
  .fact-box--heroin .fact-box__label { left: 169px; top: -30px; width: 253px; }
  .fact-box--heroin .fact-box__list { left: 29px; top: 49px; width: 500px; }
</style>
</head>
<body>
<main class="infographic">
  <header class="header">
    <div class="header-badge header-badge--left" role="img" aria-label="Prohibition sign emblem"></div>
    <div class="header-badge header-badge--right" role="img" aria-label="Syringe emblem"></div>
    <h1 class="header-title">The Introduction of Drugs to the US in the<br>19<sup>th</sup> Century</h1>
  </header>

  <div class="decor decor--molecule-top" role="img" aria-label="Morphine molecular structure diagram"></div>
  <div class="decor decor--cup" role="img" aria-label="Pill cup with tablets illustration"></div>
  <div class="decor decor--no-smoking" role="img" aria-label="No smoking sign"></div>
  <div class="decor decor--leaf" role="img" aria-label="Marijuana leaf silhouette"></div>
  <div class="decor decor--molecule-bottom" role="img" aria-label="Cocaine molecular structure diagram"></div>
  <div class="decor decor--skull" role="img" aria-label="Skull and crossbones symbol"></div>
  <div class="decor decor--no-syringe" role="img" aria-label="No syringes sign"></div>

  <section class="fact-box fact-box--morphine">
    <svg class="fact-box__frame" viewBox="0 0 557 920" preserveAspectRatio="none" aria-hidden="true">
      <defs><linearGradient id="boxFillA" x1="0" y1="0" x2="0" y2="1"><stop offset="0" stop-color="#922b45"/><stop offset="1" stop-color="#c65f74"/></linearGradient></defs>
      <polygon points="0,0 557,0 557,920 60,920 0,860" fill="url(#boxFillA)" stroke="#111" stroke-width="4" stroke-dasharray="18 6 4 6"/>
    </svg>
    <h2 class="fact-box__label">Morphine</h2>
    <ul class="fact-box__list">
      <li>originally used for medicinal purposes. It was seen as a cure-all for every imaginable ailment. to the US in the 19<sup>th</sup> Century</li>
      <li>Ironically, it was believed to be non-addictive and it was used in the treatment of curing opium addicts.</li>
      <li>Morphine was the most common pain killer used during the American Civil War. Post-war morphine addiction became so prevalent among American Civil War veterans that the drug became known as the "Soldier's Disease."</li>
    </ul>
  </section>

  <section class="fact-box fact-box--cocaine">
    <svg class="fact-box__frame" viewBox="0 0 424 1417" preserveAspectRatio="none" aria-hidden="true">
      <defs><linearGradient id="boxFillB" x1="0" y1="0" x2="0" y2="1"><stop offset="0" stop-color="#922b45"/><stop offset="1" stop-color="#c65f74"/></linearGradient></defs>
      <polygon points="0,0 380,0 424,44 424,1417 50,1417 0,1367" fill="url(#boxFillB)" stroke="#111" stroke-width="4" stroke-dasharray="18 6 4 6"/>
    </svg>
    <h2 class="fact-box__label">Cocaine</h2>
    <ul class="fact-box__list">
      <li>Was used by prominent surgeon Dr. Walter Hanley as both a local anesthesia and as a cure for his morphine addiction.</li>
      <li>Simon Fried was also a proponent of its addiction-curing powers.</li>
      <li>In 1885, John Stiles Pembrook introduced: "Vin Coca Royale--Ideal Nerve and Tonic Stimulant." This product relied heavily on extract of coca leaves. In 1886 Pembrook dubbed it "Coca-Vita." In 1906, after the federal Pure Food and Drug Act was enacted, Coca-Vita switched from using coca leaves to de-cocainized leaves.</li>
    </ul>
  </section>

  <section class="fact-box fact-box--marijuana">
    <svg class="fact-box__frame" viewBox="0 0 566 740" preserveAspectRatio="none" aria-hidden="true">
      <defs><linearGradient id="boxFillC" x1="0" y1="0" x2="0" y2="1"><stop offset="0" stop-color="#922b45"/><stop offset="1" stop-color="#c65f74"/></linearGradient></defs>
      <polygon points="40,0 566,0 566,740 40,740 0,700 0,40" fill="url(#boxFillC)" stroke="#111" stroke-width="4" stroke-dasharray="18 6 4 6"/>
    </svg>
    <h2 class="fact-box__label">Marijuana</h2>
    <ul class="fact-box__list">
      <li>It was not until the 1850s that Americans started to use marijuana for nonmedical purposes.</li>
      <li>By 1872, the United States was forced to acknowledge the rapid growth of marijuana use for purposes other than that of curative medicine.</li>
      <li>Sheer curiosity led to extreme experimental use of the drug among young professionals and even physicians.</li>
    </ul>
  </section>

  <section class="fact-box fact-box--heroin">
    <svg class="fact-box__frame" viewBox="0 0 556 906" preserveAspectRatio="none" aria-hidden="true">
      <defs><linearGradient id="boxFillD" x1="0" y1="0" x2="0" y2="1"><stop offset="0" stop-color="#922b45"/><stop offset="1" stop-color="#c65f74"/></linearGradient></defs>
      <polygon points="50,0 556,0 556,846 496,906 50,906 0,856 0,50" fill="url(#boxFillD)" stroke="#111" stroke-width="4" stroke-dasharray="18 6 4 6"/>
    </svg>
    <h2 class="fact-box__label">Heroin</h2>
    <ul class="fact-box__list">
      <li>Heroin has been known in United States history as “the last legal opiate,” and was produced commercially in 1898, by the Bauer Pharmaceutical Company.</li>
      <li>Heroin became increasingly popular over the next several years as the scientific community claimed that it was a substitute for morphine, with less addictive properties.</li>
      <li>In 1925, legislation was passed to make heroin illegal in the United States.</li>
    </ul>
  </section>
</main>
</body>
</html>
```